LUXE Medical Spa

We'd like a business card with the reverse of the card for appointments. We like round corners and vertical design. We have a background image and bird logo to include with the following wording on the front:-
Luxe Medical Spa
248 Pemberton Street
NORTH WESTBRIDGE
SA 5099
Phone 08 84391576
www.luxemedicalspa-example.com.au
Facebook luxemedicalspa
Instagram luxemedicalspa
On the back I'd like an appointment card layout please.
Cheers Dot

```html
<!DOCTYPE html>
<html lang="en">
<head>
<meta charset="utf-8">
<title>Luxe Medical Spa – Business Card</title>
<link rel="stylesheet" href="https://fonts.googleapis.com/css2?family=Arimo:wght@400;700&family=Montserrat:wght@500;600&display=swap">
<style>
  :root {
    --page: #e9ece9;
    --mint: #aad8bd;
    --ink: #161a18;
    --white: #ffffff;
    --box: #5a5f5c;
  }
  * { box-sizing: border-box; margin: 0; padding: 0; }
  html, body { width: 1200px; height: 1108px; overflow: hidden; }
  body {
    background: var(--page);
    display: flex;
    justify-content: center;
    align-items: center;
    gap: 60px;
    font-family: "Arimo", Arial, sans-serif;
    color: var(--ink);
  }
  .card {
    width: 420px;
    height: 690px;
    background: var(--mint);
    border-radius: 30px;
    position: relative;
    box-shadow: 0 10px 28px rgba(0,0,0,0.12);
    text-align: center;
  }
  .brand {
    position: absolute;
    top: 170px;
    left: 0; right: 0;
    display: flex;
    justify-content: center;
    align-items: center;
    gap: 14px;
  }
  .brand-dot {
    width: 16px; height: 16px;
    border-radius: 50%;
    background: var(--white);
  }
  .brand-name {
    font-family: "Arimo", Arial, sans-serif;
    font-weight: 400;
    font-size: 56px;
    letter-spacing: 12px;
    color: var(--white);
  }
  .brand-rule {
    position: absolute;
    top: 256px;
    left: 165px;
    width: 90px;
    height: 1px;
    background: var(--white);
  }

  /* front */
  .person { position: absolute; top: 318px; left: 0; right: 0; }
  .person-name { font-weight: 700; font-size: 26px; color: var(--white); }
  .person-role { font-size: 17px; margin-top: 4px; }
  .divider { position: absolute; left: 60px; right: 60px; height: 1px; background: var(--ink); }
  .divider.top { top: 386px; }
  .divider.bottom { top: 530px; }
  .icons {
    position: absolute; top: 376px; left: 0; right: 0;
    display: flex; justify-content: center; gap: 6px;
  }
  .icons span {
    width: 22px; height: 22px; border-radius: 50%;
    background: var(--white);
    display: flex; align-items: center; justify-content: center;
  }
  .contact { position: absolute; top: 414px; left: 0; right: 0; font-size: 18px; line-height: 24px; }
  .address { position: absolute; top: 548px; left: 0; right: 0; font-size: 18px; line-height: 23px; }

  /* back */
  .appt-title {
    position: absolute; top: 318px; left: 0; right: 0;
    font-family: "Montserrat", Arial, sans-serif;
    font-weight: 600; font-size: 22px; letter-spacing: 1px;
  }
  .appt {
    position: absolute; top: 376px; left: 48px; right: 40px;
    font-family: "Montserrat", Arial, sans-serif;
    font-weight: 500; font-size: 16px; text-align: left;
  }
  .days {
    display: grid;
    grid-template-columns: repeat(3, 1fr);
    row-gap: 16px;
  }
  .check { display: flex; align-items: center; gap: 10px; }
  .check i {
    width: 16px; height: 16px;
    border: 2px solid var(--box);
    display: inline-block;
  }
  .field { display: flex; align-items: flex-end; gap: 8px; margin-top: 22px; }
  .field .line { flex: 1; border-bottom: 1.5px solid var(--ink); height: 18px; }
  .time-row { display: flex; align-items: flex-end; gap: 16px; margin-top: 22px; }
  .time-row .line { width: 150px; border-bottom: 1.5px solid var(--ink); height: 18px; }
</style>
</head>
<body>

  <section class="card card-front">
    <div class="brand"><span class="brand-dot"></span><span class="brand-name">LUXE</span></div>
    <div class="brand-rule"></div>

    <div class="person">
      <p class="person-name">Daniel Hart</p>
      <p class="person-role">Manager</p>
    </div>
    <div class="divider top"></div>
    <div class="icons">
      <span>
        <svg width="12" height="12" viewBox="0 0 24 24" aria-label="Phone"><path fill="#aad8bd" d="M6.6 10.8a15 15 0 0 0 6.6 6.6l2.2-2.2c.3-.3.7-.4 1-.2 1.1.4 2.3.6 3.6.6.6 0 1 .4 1 1V20c0 .6-.4 1-1 1A17 17 0 0 1 3 4c0-.6.4-1 1-1h3.5c.6 0 1 .4 1 1 0 1.3.2 2.5.6 3.6.1.3 0 .7-.2 1z"/></svg>
      </span>
      <span></span>
      <span></span>
      <span></span>
    </div>
    <div class="contact">
      <p>08 84391576</p>
      <p>www.luxemedicalspa-example.com.au</p>
      <p>luxemedicalspa</p>
      <p>luxemedicalspa</p>
    </div>
    <div class="divider bottom"></div>
    <div class="address">
      <p>248 Pemberton Street</p>
      <p>NORTH WESTBRIDGE</p>
      <p>SA 5099</p>
    </div>
  </section>

  <section class="card card-back">
    <div class="brand"><span class="brand-dot"></span><span class="brand-name">LUXE</span></div>
    <div class="brand-rule"></div>

    <h2 class="appt-title">APPOINTMENT</h2>
    <div class="appt">
      <div class="days">
        <span class="check"><i></i>MON</span>
        <span class="check"><i></i>TUE</span>
        <span class="check"><i></i>WED</span>
        <span class="check"><i></i>THU</span>
        <span class="check"><i></i>FRI</span>
        <span class="check"><i></i>SAT</span>
      </div>
      <div class="field"><span>DATE</span><span class="line"></span></div>
      <div class="time-row">
        <span>TIME</span><span class="line"></span>
        <span class="check"><i></i>AM</span>
        <span class="check"><i></i>PM</span>
      </div>
    </div>
  </section>

</body>
</html>
```